BlueThistle Massage Studio

We need a double sided full colour post card sized flyer for a pro women (women only) sports and remedial massage studio based in Singapore. It's a small and boutique business promoting itself to a very local audience i.e. Within walking distance of the massage studio.

The attached logo and photo are to be integrated into the overall theme which should offer a simple, attractive, elegant and professional/sporty feel.

Funky, eclectic and/or retro options all welcome.

The company website is www.bluethistle.com.sg for reference purposes (in case Orbis Domains hasn't uploaded it yet, FB page is live; Facebook.com/bluethistlemassage). The main means of booking will be call or WhatsApp to 9381 6027 or visit the website.

Ideally there would be a white border around the postcard rather than a full bleed option.

This will be used in a mail drop environment and therefore needs to have a call to action clearly (but elegantly) displayed so as to grab attention. It needs to send the message, 'on your doorstep, female sports massage' - obviously, you have poetic license with the wording.

It is our plan that we would use a personalised stamp for special offers on the reverse side but only on one half/side - we need you to include the location map as per the web site on the other half/side.

The strap line used by Blue Thistle is 'Feel better, move better, perform better'. This should be incorporated low down, and subtly on the front side.

Target Market(s)

Women. Sports orientated. Adults, professionals and ex-pats

Industry/Entity Type

Environment

Requirements
Must have
• Call to action. Needs to be attention grabbing in a fun, elegant way

```html
<!DOCTYPE html>
<html lang="en">
<head>
<meta charset="utf-8">
<title>BlueThistle Massage Studio – Postcard</title>
<link href="https://fonts.googleapis.com/css2?family=Varela+Round&family=Open+Sans:wght@400&family=Montserrat:wght@600&family=Cormorant+SC:wght@500&family=Delius&family=Ubuntu:wght@500&family=Yanone+Kaffeesatz:wght@300&display=swap" rel="stylesheet">
<style>
  :root {
    --page: #f7f5fb;
    --card-yellow: #fbf8b6;
    --leaf-tint: #f1ecaa;
    --panel-white: #ffffff;
    --panel-leaf: #f1eefa;
    --brand: #d91ea6;
    --navy: #1c1a78;
    --ink-grey: #3a3a3a;
    --mint: #7ffad0;
    --lilac: #b99bf7;
    --lilac-soft: #cdb3f2;
    --white: #ffffff;
    --stamp-line: #111111;
  }
  * { margin: 0; padding: 0; box-sizing: border-box; }
  html, body { width: 1200px; height: 900px; overflow: hidden; background: var(--page); }
  .postcard { position: relative; width: 1200px; height: 900px; background: var(--page); }

  .card-face {
    position: absolute; left: 25px; top: 25px; width: 1150px; height: 850px;
    background:
      radial-gradient(ellipse 260px 90px at 40% 92%, var(--leaf-tint), transparent 70%),
      radial-gradient(ellipse 260px 90px at 80% 92%, var(--leaf-tint), transparent 70%),
      radial-gradient(ellipse 200px 300px at 8% 30%, var(--leaf-tint), transparent 70%),
      var(--card-yellow);
  }
  .floral-trail {
    position: absolute; left: 25px; top: 40px; width: 190px; height: 835px;
    background:
      radial-gradient(ellipse 70px 360px at 40% 55%, rgba(205,179,242,0.75), rgba(205,179,242,0) 70%),
      radial-gradient(ellipse 150px 120px at 35% 95%, rgba(205,179,242,0.8), rgba(205,179,242,0) 70%),
      radial-gradient(ellipse 50px 90px at 45% 8%, rgba(205,179,242,0.6), rgba(205,179,242,0) 70%);
  }
  .address-panel {
    position: absolute; left: 655px; top: 25px; width: 520px; height: 728px;
    background:
      radial-gradient(ellipse 220px 260px at 30% 35%, var(--panel-leaf), transparent 70%),
      radial-gradient(ellipse 220px 260px at 75% 75%, var(--panel-leaf), transparent 70%),
      var(--panel-white);
  }
  .stamp-box {
    position: absolute; left: 948px; top: 28px; width: 226px; height: 229px;
    border: 4px solid var(--stamp-line); background: var(--panel-white);
  }

  .brand-name {
    position: absolute; left: 130px; top: 40px;
    font-family: "Varela Round", sans-serif; font-weight: 400; font-size: 90px; line-height: 1;
    color: var(--brand); letter-spacing: 2px;
  }
  .brand-tagline {
    position: absolute; left: 132px; top: 134px;
    font-family: "Open Sans", sans-serif; font-size: 27px; color: var(--ink-grey);
  }
  .studio-address {
    position: absolute; left: 148px; top: 178px;
    font-family: "Montserrat", sans-serif; font-weight: 600; font-size: 32px; color: var(--navy);
    letter-spacing: 0.5px;
  }
  .studio-phone {
    position: absolute; left: 228px; top: 213px;
    font-family: "Montserrat", sans-serif; font-weight: 600; font-size: 25px; color: var(--navy);
    letter-spacing: 2.5px;
  }

  .offer-frame {
    position: absolute; left: 165px; top: 256px; width: 488px; height: 470px;
    background: var(--mint); border-radius: 34px 0 24px 0;
  }
  .offer-audience {
    position: absolute; left: 165px; top: 272px; width: 510px; text-align: center;
    font-family: "Cormorant SC", serif; font-weight: 500; font-size: 34px; color: var(--white);
  }
  .offer-service {
    position: absolute; left: 228px; top: 313px;
    font-family: "Delius", cursive; font-style: italic; font-size: 27px; line-height: 37px;
    color: var(--white); letter-spacing: 5px; white-space: nowrap;
  }
  .offer-card {
    position: absolute; left: 180px; top: 400px; width: 453px; height: 310px;
    background: var(--lilac); border-radius: 28px 0 36px 0;
  }
  .offer-heading {
    position: absolute; left: 207px; top: 428px;
    font-family: "Cormorant SC", serif; font-weight: 500; font-size: 42px; color: var(--white);
    white-space: nowrap;
  }
  .strapline {
    position: absolute; left: 283px; top: 484px;
    font-family: "Ubuntu", sans-serif; font-weight: 500; font-size: 42px; line-height: 53px;
    color: var(--white); white-space: nowrap;
  }
  .offer-note {
    position: absolute; left: 232px; top: 656px;
    font-family: "Yanone Kaffeesatz", sans-serif; font-weight: 300; font-size: 38px;
    color: var(--white); letter-spacing: 0.6px; white-space: nowrap;
  }
</style>
</head>
<body>
  <main class="postcard">
    <div class="card-face" role="img" aria-label="Pale yellow card with a faint repeating leaf pattern"></div>
    <div class="floral-trail" role="img" aria-label="Lilac floral swirl ornament with small flowers and dots"></div>
    <div class="address-panel" role="img" aria-label="White address side with a faint lilac leaf pattern"></div>
    <div class="stamp-box" aria-label="Stamp area"></div>

    <h1 class="brand-name">bluethistle</h1>
    <p class="brand-tagline">Remedial and sports massage</p>
    <p class="studio-address">18 Cassia Lane, Singapore</p>
    <p class="studio-phone">(+65) 9381 6027</p>

    <div class="offer-frame"></div>
    <p class="offer-audience">WOMEN-ONLY,</p>
    <p class="offer-service">Boutique Remedial And<br>Sports Massage Service</p>

    <div class="offer-card"></div>
    <p class="offer-heading">We are special offers,</p>
    <p class="strapline">Move better,<br>Feel better and<br>Perform better.</p>
    <p class="offer-note">Provided By Only Our Industry</p>
  </main>
</body>
</html>
```